Three Ebook Covers for Short Stories

Three Ebook cover designs for 3 short stories (all linked) psychological thriller. I like clean crisp images. Perhaps with an imagine of eyes/part of face - white woman, 29, thin, brown eyes, short bob hair. I like gritty, moody, raw type of images. I dont mind the same image being used on three covers providing there are differences (ie slight variation in colour of book). Colours I prefer red, burgundy, black, grey, white. My website shows off the type of colours I prefer. www.lydiakbarnes-author.net
Branding is important.

Target Market(s)

Adult. Moth in Attic, Lost Field, type of readers.

Industry/Entity Type

Book Publisher

Font styles to use
Sans Serif
Other font styles liked:
• fonts used on thriller novels

Requirements
Must have
• Author Name: Lydia K Barnes
• Short Story as Part of Title
• Short Story 1: Title - First Crow
• Short Story 2: Title - Second Crow
• Short Story 3: Title - Third Crow
• Branding is important so they must look like they are a set.
• A font which is aligned to thriller type novels
• Colours aligned to my website - red, burgundy, white, grey, black.
Nice to have
• I don't mind a black and white type photo imagine.
Should not have
• n/a

```html
<!DOCTYPE html>
<html lang="en">
<head>
<meta charset="utf-8">
<title>First Crow · Second Crow · Third Crow — Lydia K Barnes</title>
<link rel="stylesheet" href="https://fonts.googleapis.com/css2?family=Bebas+Neue&family=Oswald:wght@500&display=swap">
<style>
  :root {
    --paper: #ffffff;
    --ink: #050505;
    --title: #f4f4f2;
    --author: #f2c200;
    --skin: #d9d3cc;
    --skin-shadow: #8e847c;
    --hair-red: #7a0d12;
    --hair-black: #141414;
    --hair-teal: #1f5a5a;
  }
  * { margin: 0; padding: 0; box-sizing: border-box; }
  html, body {
    width: 1200px; height: 594px; overflow: hidden;
    background: var(--paper);
  }
  .cover-set {
    display: flex; justify-content: space-between;
    width: 1200px; height: 594px;
  }
  .cover {
    position: relative;
    width: 392px; height: 594px;
    overflow: hidden;
    background: var(--ink);
  }
  .cover-art {
    position: absolute; inset: 0 0 auto 0; height: 430px;
  }
  .cover--first .cover-art {
    background:
      radial-gradient(ellipse 34% 46% at 50% 34%, var(--skin) 0%, var(--skin-shadow) 70%, transparent 100%),
      linear-gradient(90deg, var(--hair-red) 0%, #3a0508 30%, #2a2320 50%, #3a0508 70%, var(--hair-red) 100%);
  }
  .cover--second .cover-art {
    background:
      radial-gradient(ellipse 34% 46% at 50% 34%, var(--skin) 0%, var(--skin-shadow) 70%, transparent 100%),
      linear-gradient(90deg, var(--hair-black) 0%, #2a2a2a 30%, #bdbdbd 50%, #2a2a2a 70%, var(--hair-black) 100%);
  }
  .cover--third .cover-art {
    background:
      radial-gradient(ellipse 34% 46% at 50% 34%, var(--skin) 0%, var(--skin-shadow) 70%, transparent 100%),
      linear-gradient(90deg, var(--hair-teal) 0%, #0f2c2c 30%, #2a3332 50%, #0f2c2c 70%, var(--hair-teal) 100%);
  }
  .cover-fade {
    position: absolute; left: 0; right: 0; top: 280px; height: 180px;
    background: linear-gradient(180deg, rgba(5,5,5,0) 0%, rgba(5,5,5,0.75) 55%, var(--ink) 100%);
  }
  .cover-title {
    position: absolute; left: 0; right: 0; top: 318px;
    font-family: "Bebas Neue", "Oswald", sans-serif;
    font-weight: 400;
    color: var(--title);
    text-align: center;
    line-height: 0.74;
    font-size: 146px;
  }
  .cover-title span { display: block; }
  .title-line--wide { letter-spacing: 0.14em; padding-left: 0.14em; }
  .title-line--mid { letter-spacing: 0.06em; padding-left: 0.06em; }
  .title-line--tight { letter-spacing: 0.01em; padding-left: 0.01em; font-size: 128px; }
  .cover-series {
    position: absolute; left: 0; right: 0; top: 548px;
    font-family: "Oswald", sans-serif; font-weight: 500;
    font-size: 12px; letter-spacing: 0.22em;
    color: var(--title); text-align: center;
  }
  .cover-author {
    position: absolute; left: 0; right: 0; top: 562px;
    font-family: "Oswald", sans-serif; font-weight: 500;
    font-size: 24px; letter-spacing: 0.04em; line-height: 1.1;
    color: var(--author); text-align: center;
  }
</style>
</head>
<body>
  <main class="cover-set">
    <article class="cover cover--first">
      <div class="cover-art" role="img" aria-label="Close-up portrait photograph of a young woman with a red bob haircut and dark red lips"></div>
      <div class="cover-fade"></div>
      <h2 class="cover-title"><span class="title-line--wide">FIRST</span><span class="title-line--wide">CROW</span></h2>
      <p class="cover-series">SHORT STORY 1</p>
      <p class="cover-author">LYDIA K BARNES</p>
    </article>
    <article class="cover cover--second">
      <div class="cover-art" role="img" aria-label="Close-up portrait photograph of a young woman with a black bob haircut and dark red lips"></div>
      <div class="cover-fade"></div>
      <h2 class="cover-title"><span class="title-line--tight">SECOND</span><span class="title-line--wide">CROW</span></h2>
      <p class="cover-series">SHORT STORY 2</p>
      <p class="cover-author">LYDIA K BARNES</p>
    </article>
    <article class="cover cover--third">
      <div class="cover-art" role="img" aria-label="Close-up portrait photograph of a young woman with a teal bob haircut and dark lips"></div>
      <div class="cover-fade"></div>
      <h2 class="cover-title"><span class="title-line--mid">THIRD</span><span class="title-line--wide">CROW</span></h2>
      <p class="cover-series">SHORT STORY 3</p>
      <p class="cover-author">LYDIA K BARNES</p>
    </article>
  </main>
</body>
</html>
```